Web Design needed for logo design project

I am needing an interactive website for BC. Talvor Care Management is a nationwide company that combines the front desk administrative operation within Professional offices (Dental, Chiropractic, Optometry). I am needing a website designed that will provide information for potential new clients that are interested in joining our company to provide to them administrative support. I need a design for the marketing material within the folder, I will add content later. I am looking for clean crisp professional. No dancing teeth, hearts, or EKG signals please. We need it to appeal to 27-40 years old professionals. The professions are equally divided at 50/50 female to male. I already have a logo, it will be attached.
Updates

Target Market(s)

We need it to appeal to 27-40 years old professionals. The professions are equally divided at 50/50 female to male. I already have a logo, it will be attached.

Industry/Entity Type

Marketing

Requirements
Must have
• Needs to be in Word Press. It must have scalability to various screen sizes (Monitor, Phone screen, IPad, etc). Must have a customer portal capability, so professionals can access their information through a portal on the website. Have the capability to run a practice calculator or view a video requiring that it captures the visitors information so I can contact them regarding their interest in the site. Needs to have links to social media.

```html
<!DOCTYPE html>
<html lang="en">
<head>
<meta charset="utf-8">
<title>Talvor Care Management</title>
<link href="https://fonts.googleapis.com/css2?family=Fira+Sans:wght@400;600;700&display=swap" rel="stylesheet">
<style>
  :root {
    --page-bg: #eeeeee;
    --panel-bg: #ffffff;
    --panel-border: #c6c6c6;
    --brand-navy: #0b3f73;
    --brand-sky: #3aa6dd;
    --nav-top: #0b4d88;
    --nav-bottom: #003868;
    --ink: #151a26;
    --body-ink: #1d1d1d;
    --white: #ffffff;
    --headline-box: rgba(34, 34, 36, 0.88);
    --button-bg: rgba(18, 64, 112, 0.85);
  }
  * { box-sizing: border-box; margin: 0; padding: 0; }
  html, body {
    width: 1200px; height: 990px; overflow: hidden;
    background: var(--page-bg);
    font-family: "Fira Sans", Arial, sans-serif;
  }
  body { position: relative; }
  .site-header {
    height: 114px;
    display: flex; align-items: center; justify-content: center; gap: 12px;
  }
  .brand-mark { width: 18px; height: 18px; background: var(--brand-navy); }
  .brand-name {
    font-size: 28px; font-weight: 600; color: var(--brand-navy);
    letter-spacing: 1px; text-transform: uppercase;
  }
  .page-panel {
    position: absolute; left: 99px; top: 114px; width: 1013px; height: 876px;
    overflow: hidden;
    background: var(--panel-bg);
    border: 1px solid var(--panel-border); border-bottom: none;
  }
  .hero {
    position: relative; height: 484px;
    background: linear-gradient(90deg, #3a3b3d 0%, #55585b 35%, #cfd3d2 62%, #eef0ef 80%, #d8dcdb 100%);
  }
  .hero-headline {
    position: absolute; left: 67px; top: 111px; width: 431px; height: 205px;
    background: var(--headline-box);
    padding: 14px 14px;
    color: var(--white); font-size: 56px; font-weight: 600; line-height: 60px;
  }
  .hero-button {
    position: absolute; left: 67px; top: 332px; width: 245px; height: 46px;
    border-radius: 23px; background: var(--button-bg);
    color: var(--white); font-size: 15px; font-weight: 600; letter-spacing: 0.5px;
    display: flex; align-items: center; justify-content: center;
    text-decoration: none;
  }
  .main-nav {
    height: 48px;
    background: linear-gradient(var(--nav-top), var(--nav-bottom));
    display: flex; align-items: center; justify-content: center; gap: 14px;
  }
  .main-nav a {
    color: var(--white); font-size: 17px; font-weight: 600; letter-spacing: 0.5px;
    text-decoration: none;
  }
  .main-nav a.is-active { color: var(--brand-sky); }
  .nav-dot { width: 8px; height: 8px; border: 1px solid #c7d6e6; border-radius: 50%; }
  .intro-title {
    margin-top: 40px; text-align: center;
    font-size: 27px; font-weight: 600; color: var(--ink); letter-spacing: 0.3px;
  }
  .service-icons {
    margin-top: 48px; margin-right: 56px;
    display: flex; justify-content: center; gap: 24px;
  }
  .service-icon {
    width: 100px; height: 100px; border-radius: 50%;
    border: 2px solid #e2e2e2;
  }
  .service-icon.support { background: radial-gradient(circle at 50% 45%, #f1d6c6, #d9d9d9 70%); }
  .service-icon.patients { background: radial-gradient(circle at 50% 45%, #e3b99c, #9aa884 75%); }
  .service-icon.wellness { background: radial-gradient(circle at 50% 45%, #6cc240, #f3f3f3 72%); }
  .intro-copy {
    width: 890px; margin: 46px auto 0; text-align: center;
    font-size: 14.2px; line-height: 18px; color: var(--body-ink);
  }
  .intro-copy p + p { margin-top: 18px; }
  .intro-copy strong { font-weight: 700; }
  .intro-copy a { color: var(--brand-sky); text-decoration: none; }
</style>
</head>
<body>
  <header class="site-header">
    <span class="brand-mark"></span>
    <span class="brand-name">Talvor Care Management</span>
  </header>

  <div class="page-panel">
    <section class="hero" role="img" aria-label="Photo of a smiling office administrator wearing a headset at a computer">
      <h1 class="hero-headline">we provide you administrative support.</h1>
      <a class="hero-button" href="#about">LEARN MORE ABOUT US</a>
    </section>

    <nav class="main-nav">
      <a href="#home">HOME</a><span class="nav-dot"></span>
      <a href="#join" class="is-active">JOINING THE COMPANY</a><span class="nav-dot"></span>
      <a href="#about">ABOUT US</a><span class="nav-dot"></span>
      <a href="#services">SERVICES</a><span class="nav-dot"></span>
      <a href="#contact">CONTACT</a>
    </nav>

    <h2 class="intro-title">What we do at talvor care management.</h2>

    <div class="service-icons">
      <div class="service-icon support" role="img" aria-label="Photo of a front desk assistant with a headset"></div>
      <div class="service-icon patients" role="img" aria-label="Photo of a smiling senior patient"></div>
      <div class="service-icon wellness" role="img" aria-label="Photo of a green apple with a stethoscope"></div>
    </div>

    <div class="intro-copy">
      <p><strong>There are many variations of passages</strong> of Lorem Ipsum available, but the <a href="#services">majority have suffered alteration</a> in some form, by injected humour, or randomised words which don't look even slightly believable. If you are going to use a passage of Lorem Ipsum, you need to be sure there isn't anything embarrassing hidden in the middle of text.</p>
      <p><strong>All the Lorem Ipsum generators on the Internet tend to repeat predefined</strong> chunks as necessary, making this the first true generator on</p>
    </div>
  </div>
</body>
</html>
```